■依頼の目的/概要
電子書籍の表紙デザインをお願いします。

経営者のための「黄金オフィス気学」
〜歴史に名を遺す名将や成功者はみんなやっていた〜

著者
経営者専属:開運鑑定士 夕凪みのり

★読者限定プレゼント→今すぐあなたや社員の吉方位が分かる「本命掛早見表と八宅盤」

■本の内容
経営者向けの経営サポート本として「ビジネス風水」を具体的にご紹介しています。
「まえがき、目次、本文、後書き」原稿をファイル添付していますので、まえがきや目次等見ていただき、内容の雰囲気をご確認いただけると嬉しいです。

筆者(私)はタロット歴20年の電話占い師(夕凪みのり)です。本書の著者の肩書きは↑にも書いておりますように「経営者専属:開運鑑定士 夕凪みのり」でお願い致します。

■デザイン要望
経営者に魅力を感じていただきやすくパッと目を引き、どのような本なのかが一目で分かりやすいデザインが望ましいです。基本全部おまかせです。是非デザイナーさんの魅力と才能を発揮していただけたらと思います。

その他何かご不明な点がございましたら、お気軽にご質問下さい。
よろしくお願いいたします。
【画像サイズ】※RLQより抜粋(電子書籍はLumoraです)
表紙ファイルの理想的な寸法は、2,560✖️1,600ピクセルです。
注:画像の寸法は、1,000✖️625ピクセル以上であることが必要です。
画像の最大の寸法は、10,000✖️10,000ピクセルです。

Zentaro(Lumora)に表示された際はかなり小さくなる事を踏まえ、他の経営者向けの本と並んだ時、目が止まりやすい一冊になるか?という点を意識し、選ばさせて頂きました。

表紙デザインの色や見た目のインパクトと文字の分かりやすさ、サブタイトルまでしっかりアピールされている所が気に入りました。

クラフターの皆様、この度はコンペにご参加いただきまして誠にありがとうございました。
本当に素晴らしいデザインばかりで、正直選考はとても難航いたしました。

今回は沢山のご提案の中から1つを選ぶことがとても難しかった為「他の経営者向けの本と並んだ時、目が止まりやすい一冊になるか?内容が分かりやすいか?」を軸に、著者仲間30名にアンケートを実施し当選作品を決定させて頂きました。

改めまして、皆様の才能を発揮して頂き素晴らしい作品をご提案頂きました事、心より感謝申し上げます。誠にありがとうございました。

```html
<!DOCTYPE html>
<html lang="ja">
<head>
<meta charset="utf-8">
<title>経営者のための黄金オフィス気学</title>
<link href="https://fonts.googleapis.com/css2?family=Noto+Sans+JP:wght@400;700;900&family=Noto+Serif+JP:wght@600;700;900&display=swap" rel="stylesheet">
<style>
  :root{
    --brand-blue:#1f63c9;
    --band-top:#3d86e6;
    --band-bottom:#1c5fc4;
    --panel:rgba(22,52,120,0.86);
    --ink:#141414;
    --white:#ffffff;
    --frame:#e9c84a;
  }
  *{margin:0;padding:0;box-sizing:border-box}
  html,body{width:750px;height:1200px;overflow:hidden;background:#fff}
  .cover{position:relative;width:750px;height:1200px;overflow:hidden;font-family:"Noto Sans JP",sans-serif;color:var(--ink)}
  .bg-city{position:absolute;inset:0;background:linear-gradient(180deg,#f4f6f8 0%,#e3e7ec 35%,#cfd5dc 60%,#b9c0c8 100%)}
  .bg-compass{position:absolute;left:0;top:930px;width:612px;height:270px;
    background:radial-gradient(ellipse at 45% 70%,#d9b765 0%,#a8802f 45%,#5b4218 100%)}
  .side-band{position:absolute;left:612px;top:0;width:138px;height:1200px;
    background:linear-gradient(180deg,var(--band-top),var(--band-bottom))}
  .subtitle{position:absolute;left:658px;top:40px;writing-mode:vertical-rl;white-space:nowrap;
    font-family:"Noto Serif JP",serif;font-weight:700;font-size:46px;line-height:1;color:var(--white)}
  .author-role{position:absolute;left:48px;top:28px;font-weight:900;font-size:26px;line-height:1.4;color:var(--brand-blue)}
  .author-name{position:absolute;left:150px;top:74px;font-weight:700;font-size:27px;line-height:1.4;color:var(--brand-blue)}
  .title{position:absolute;left:0;width:612px;text-align:center;font-family:"Noto Serif JP",serif;font-weight:900;line-height:1;white-space:nowrap}
  .title-lead{top:232px;font-size:50px;color:var(--ink)}
  .title-main{top:290px;font-size:70px;color:var(--ink);letter-spacing:2px}
  .title-key{top:365px;font-size:108px;color:var(--brand-blue);letter-spacing:14px;padding-left:14px}
  .quote-panel{position:absolute;left:0;top:492px;width:612px;height:512px;background:var(--panel);
    padding:24px 20px 0 22px;color:var(--white);font-weight:700;font-size:20.5px;line-height:41px;white-space:nowrap}
  .gift{position:absolute;left:95px;top:1012px;width:405px;height:128px;background:rgba(255,255,255,0.95);
    border:4px solid var(--frame);border-radius:14px;text-align:center;padding-top:8px}
  .gift-label{font-weight:900;font-size:22px;color:var(--brand-blue);line-height:34px}
  .gift-text{font-weight:700;font-size:17px;color:var(--ink);line-height:28px}
  .gift-title{font-weight:900;font-size:24px;color:var(--brand-blue);line-height:38px}
</style>
</head>
<body>
<div class="cover">
  <div class="bg-city" role="img" aria-label="オフィスビル群を見上げた写真"></div>
  <div class="bg-compass" role="img" aria-label="金色の風水羅盤の写真"></div>

  <div class="side-band"></div>
  <p class="subtitle">〜歴史に名を遺す名将や成功者はみんなやっていた〜</p>

  <p class="author-role">経営者専属：開運鑑定士</p>
  <p class="author-name">夕凪みのり 著</p>

  <h1>
    <span class="title title-lead">経営者のための</span>
    <span class="title title-main">黄金オフィス</span>
    <span class="title title-key">気学</span>
  </h1>

  <div class="quote-panel">
    J.R.ハーグレイヴ氏は、米５大財閥の一つである<br>
    ハーグレイヴ財閥の創始者で「金融王」とも呼ばれる大富豪。<br>
    ハーグレイヴ氏は３０年前のニューアーク・クロニクルで<br>
    『億万長者は星占術を信じないが、大富豪は活用<br>
    するのだ』<br>
    と公言しており、占いに人生を左右される<br>
    わけではないものの<br>
    「真の大金持ちこそ占星術を信じるものだ」<br>
    といった意味ともとれる、深い言葉を残しています。
  </div>

  <div class="gift">
    <p class="gift-label">★読者限定プレゼント</p>
    <p class="gift-text">今すぐあなたや社員の吉方位が分かる</p>
    <p class="gift-title">「本命掛早見表と八宅盤」</p>
  </div>
</div>
</body>
</html>
```